KMT Law Firm Business Card

We need a business card design for our law firm. We recently had a name change and so we have a new logo. We are a small plaintiff's law firm in Oklahoma but do work all over the USA We have a new logo (see attached the artwork in both black & brown – could also reverse the logo so that it’s white) We'd like an upscale western design. One side needs the logo and this slogan : "Courage-Conviction-Care Always stand for you"
and on the other side needs to be a template so we can fill in the attorney's name --include this info:
Whitcombe Whitcombe Delacroix
-------Attorneys------------
(name of attorney) ie: Howard T. Whitcombe
(title) ie: Attorney/Managing Partner
5812 S. Garnet Tulsa, OK 74139
918-555-0143
Fax 918-555-0178
(name)@kmtlegal.example www.kmtlegal.example ie: hank@kmtlegal.example
also needs a small Facebook & twitter logo -
and 3 of the attorneys need the circle logo attached that says "Grand Verdict Litigators Circle" - so we need to be able to remove that for some of the designs –

Industry/Entity Type

Law Firm

```html
<!DOCTYPE html>
<html lang="en">
<head>
<meta charset="utf-8">
<title>Whitcombe Whitcombe Delacroix – Business Card</title>
<link href="https://fonts.googleapis.com/css2?family=Lato:wght@400;700;900&display=swap" rel="stylesheet">
<style>
  :root {
    --stage: #dbe6f7;
    --paper: #ffffff;
    --ink: #111111;
    --night: #050505;
    --light: #f4f4f4;
    --badge: #7a1620;
    --social: #3b5a9a;
  }
  * { margin: 0; padding: 0; box-sizing: border-box; }
  html, body { width: 1200px; height: 965px; overflow: hidden; }
  body {
    position: relative;
    background: var(--stage);
    font-family: 'Lato', sans-serif;
    color: var(--ink);
  }
  .card {
    position: absolute;
    width: 630px;
    height: 360px;
    border-radius: 22px;
    overflow: hidden;
  }
  .card--front { left: 285px; top: 80px; background: var(--paper); }
  .card--back { left: 285px; top: 524px; width: 629px; background: var(--night); color: var(--light); }

  .badge {
    position: absolute;
    width: 92px; height: 92px;
    border-radius: 50%;
    background: var(--badge);
  }
  .card--front .badge { left: 32px; top: 32px; }
  .card--back .badge { left: 526px; top: 15px; }

  .firm-mark {
    position: absolute;
    text-align: center;
    font-weight: 900;
    text-transform: uppercase;
    line-height: 1.15;
  }
  .card--front .firm-mark { left: 395px; top: 52px; width: 230px; font-size: 22px; color: var(--ink); }
  .card--back .firm-mark { left: 165px; top: 108px; width: 300px; font-size: 28px; color: var(--light); }

  .attorney { position: absolute; left: 33px; top: 168px; }
  .attorney__name { font-weight: 700; font-size: 19px; font-variant: small-caps; letter-spacing: 0.2px; }
  .attorney__title { font-size: 15px; margin-top: 2px; }

  .rule { position: absolute; left: 33px; right: 24px; top: 227px; height: 2px; background: var(--ink); }

  .contacts { position: absolute; left: 33px; top: 249px; list-style: none; font-size: 15px; line-height: 18.5px; }
  .contacts li { display: flex; align-items: center; gap: 3px; }
  .contacts svg { width: 17px; height: 14px; fill: var(--ink); }

  .address { position: absolute; right: 24px; top: 256px; text-align: right; font-size: 15px; line-height: 18.5px; font-style: normal; }
  .social { position: absolute; right: 24px; top: 300px; display: flex; align-items: center; gap: 5px; font-size: 15px; }
  .social__label { margin-right: 8px; }
  .social__dot { width: 15px; height: 15px; border-radius: 50%; background: var(--social); }

  .slogan {
    position: absolute; left: 0; right: 0; top: 300px;
    text-align: center;
    font-size: 24px;
    font-variant: small-caps;
    letter-spacing: 0.6px;
    color: var(--light);
  }
</style>
</head>
<body>
  <section class="card card--front" aria-label="Business card front">
    <div class="badge" role="img" aria-label="Grand Verdict Litigators Circle member badge"></div>
    <div class="firm-mark">Whitcombe<br>Whitcombe<br>Delacroix</div>

    <div class="attorney">
      <p class="attorney__name">Howard T. Whitcombe</p>
      <p class="attorney__title">Attorney/Managing Partner</p>
    </div>

    <div class="rule"></div>

    <ul class="contacts">
      <li><svg viewBox="0 0 16 14" aria-hidden="true"><path d="M1 4c0-2 3-3 7-3s7 1 7 3v1h-4V4H5v1H1zM4 6h8l2 7H2z"/></svg>918-555-0143</li>
      <li><svg viewBox="0 0 16 14" aria-hidden="true"><path d="M4 0h8v4H4zM1 5h14v6h-3v3H4v-3H1zM5 9v4h6V9z"/></svg>918-555-0178</li>
      <li><svg viewBox="0 0 16 14" aria-hidden="true"><path d="M1 2h14v10H1zM2.5 3.5 8 8l5.5-4.5v-.1H2.5z" fill-rule="evenodd"/></svg>hank@kmtlegal.example</li>
      <li><svg viewBox="0 0 16 14" aria-hidden="true"><path d="M1 1h14v9H1zM2.5 2.5v6h11v-6zM5 11h6v2H5z" fill-rule="evenodd"/></svg>www.kmtlegal.example</li>
    </ul>

    <address class="address">5812 S. Garnet Tulsa<br>OK 74139</address>
    <div class="social">
      <span class="social__label">Contact Us</span>
      <span class="social__dot" role="img" aria-label="Social profile link"></span>
      <span class="social__dot" role="img" aria-label="Social profile link"></span>
    </div>
  </section>

  <section class="card card--back" aria-label="Business card back">
    <div class="badge" role="img" aria-label="Grand Verdict Litigators Circle member badge"></div>
    <div class="firm-mark">Whitcombe<br>Whitcombe<br>Delacroix</div>
    <p class="slogan">Courage-Conviction-Care Always stand for you</p>
  </section>
</body>
</html>
```